CD-/Plattencover für eine Tonträgerfirma
Zielgruppe
Wir sind eine Tonträgerfirma und bewegen uns im Low-Budget-Segment.
Aufgabenstellung
'Harbor Lanterns'
Wir benötigen nicht das komplette Artwork, sondern ein Frontcover
(121 x 120 mm + 20 mm Beschnitt) wg. etwaiger Verschiebung der Positionierung.
Fertigstellung (Aufziehen des Inlays und Labels) erfolgt später bei uns im Hause.
Wir benötigen später eine offene psd-Datei mit allen Ebenen.
Wichtig: Schriften nicht gerastert ggfs. Schrift mitliefern.
Was wir uns vorstellen:
- Entsprechend der Musik Bild
- Da es ein 2-CD-Set ist, sollte '2 CDs' auch gut auf dem Cover ersichtlich sein
- Folgende Titel sollten auf dem Cover genannt werden
Rowan Lad
Hills of Fern
Gentle Harrow
- Bildmaterial sollte bei pixelbarn, bildora oder n-pics ausgesucht werden,
das Bildmaterial wird dann später auch von uns dort eingekauft
- keine Künstlerfotos
- vorzugsweise nur 1 Bild pro Layout, max. 2 Bilder
Wir freuen uns und sind sehr gespannt auf eure Vorschläge,
bei Fragen gerne mailen

```html
<!DOCTYPE html>
<html lang="en">
<head>
<meta charset="utf-8">
<title>Harbor Lanterns – 2CD Set</title>
<link rel="stylesheet" href="https://fonts.googleapis.com/css2?family=Cinzel+Decorative:wght@700&family=Playfair+Display:ital,wght@1,700&family=Open+Sans:wght@600;800&display=swap">
<style>
  :root {
    --paper: #f2f2f2;
    --frame-line: #c4c4c4;
    --ornament-grey: #d4d4d4;
    --ring-dark: #1f6b24;
    --ring-mid: #2f8a2c;
    --ring-light: #56c33c;
    --ring-edge: #ffffff;
    --sky: #9fb7d2;
    --sea: #1d4f7e;
    --cliff: #6b5a3c;
    --grass: #4f8a2a;
    --title: #ffffff;
    --title-shadow: rgba(0,0,0,0.55);
    --caption: #ffffff;
    --set-label: #4a4a4a;
  }
  html, body {
    margin: 0;
    padding: 0;
    overflow: hidden;
    background: var(--paper);
  }
  .cover {
    position: relative;
    width: 1200px;
    height: 1194px;
    background: var(--paper);
  }
  .cover svg { display: block; }
  .frame-line { stroke: var(--frame-line); stroke-width: 3; fill: none; }
  .corner-ornament { fill: var(--ornament-grey); }
  .ring-outer { fill: var(--ring-dark); }
  .ring-edge { fill: none; stroke: var(--ring-edge); stroke-width: 6; }
  .ring-inner-edge { fill: none; stroke: var(--ring-dark); stroke-width: 10; }
  .title-main {
    font-family: "Cinzel Decorative", serif;
    font-weight: 700;
    font-size: 150px;
    fill: var(--title);
    letter-spacing: -2px;
  }
  .title-sub {
    font-family: "Playfair Display", serif;
    font-style: italic;
    font-weight: 700;
    font-size: 84px;
    fill: var(--title);
  }
  .track-list {
    font-family: "Open Sans", sans-serif;
    font-weight: 600;
    font-size: 22px;
    fill: var(--caption);
    letter-spacing: 0.5px;
  }
  .set-label {
    font-family: "Open Sans", sans-serif;
    font-weight: 800;
    font-size: 28px;
    fill: var(--set-label);
    letter-spacing: 3px;
  }
</style>
</head>
<body>
<main class="cover">
  <svg width="1200" height="1194" viewBox="0 0 1200 1194" xmlns="http://www.w3.org/2000/svg">
    <defs>
      <radialGradient id="ringBand" cx="50%" cy="50%" r="50%">
        <stop offset="70%" stop-color="var(--ring-mid)"/>
        <stop offset="85%" stop-color="var(--ring-light)"/>
        <stop offset="100%" stop-color="var(--ring-mid)"/>
      </radialGradient>
      <linearGradient id="coastScene" x1="0" y1="0" x2="1" y2="1">
        <stop offset="0%" stop-color="var(--sky)"/>
        <stop offset="30%" stop-color="var(--sky)"/>
        <stop offset="45%" stop-color="var(--cliff)"/>
        <stop offset="60%" stop-color="var(--sea)"/>
        <stop offset="80%" stop-color="var(--cliff)"/>
        <stop offset="100%" stop-color="var(--grass)"/>
      </linearGradient>
      <filter id="titleShadow" x="-10%" y="-20%" width="120%" height="140%">
        <feDropShadow dx="3" dy="4" stdDeviation="4" flood-color="var(--title-shadow)"/>
      </filter>
    </defs>

    <g class="frame">
      <line class="frame-line" x1="320" y1="82" x2="880" y2="82"/>
      <line class="frame-line" x1="300" y1="1108" x2="470" y2="1108"/>
      <line class="frame-line" x1="730" y1="1108" x2="900" y2="1108"/>
      <line class="frame-line" x1="92" y1="300" x2="92" y2="900"/>
      <line class="frame-line" x1="1108" y1="300" x2="1108" y2="900"/>
    </g>

    <g role="img" aria-label="Grey Celtic knot ornaments in the four corners">
      <ellipse class="corner-ornament" cx="160" cy="150" rx="60" ry="40" opacity="0.6"/>
      <ellipse class="corner-ornament" cx="1040" cy="150" rx="60" ry="40" opacity="0.6"/>
      <ellipse class="corner-ornament" cx="160" cy="1050" rx="60" ry="40" opacity="0.6"/>
      <ellipse class="corner-ornament" cx="1040" cy="1050" rx="60" ry="40" opacity="0.6"/>
    </g>

    <circle class="ring-outer" cx="600" cy="600" r="482"/>
    <circle cx="600" cy="600" r="462" fill="url(#ringBand)" role="img" aria-label="Ring of green Celtic interlace pattern"/>
    <circle class="ring-edge" cx="600" cy="600" r="470"/>

    <circle cx="600" cy="600" r="345" fill="var(--ring-dark)"/>
    <circle cx="600" cy="600" r="336" fill="url(#coastScene)" role="img" aria-label="Photo of steep green-topped sea cliffs above a deep blue ocean"/>
    <circle class="ring-inner-edge" cx="600" cy="600" r="340"/>

    <g class="title" filter="url(#titleShadow)">
      <text class="title-main" x="600" y="620" text-anchor="middle">Harbor</text>
      <text class="title-sub" x="915" y="730" text-anchor="end">lanterns</text>
    </g>

    <g class="track-list">
      <text x="600" y="842" text-anchor="middle">ROWAN LAD  •  HILLS OF FERN</text>
      <text x="600" y="886" text-anchor="middle">GENTLE HARROW</text>
    </g>

    <text class="set-label" x="600" y="1118" text-anchor="middle">2CD SET</text>
  </svg>
</main>
</body>
</html>
```